Need Letterhead and Business Card

I have a logo but i need new letterhead and biz cards. We are a real estate investment firm so we need very professional but also do not want to be old fashioned. We have 3 locations; Singapore, New York and Ponte Vedra Florida. I can provide full addresses if needed. If you have adjustments to our logo you would recommend we are open to them.
I will be putting in a separate project but we also need a template for our own powerpoint slide presentations and website.

Industry/Entity Type

Real Estate

```html
<!DOCTYPE html>
<html lang="en">
<head>
<meta charset="utf-8">
<title>Halden Business Card</title>
<link rel="stylesheet" href="https://fonts.googleapis.com/css2?family=Open+Sans:wght@400;600;700&display=swap">
<style>
  :root {
    --navy: #14497c;
    --gold: #c0952f;
    --ink: #2a2a2a;
    --paper: #ffffff;
    --backdrop: #161719;
  }
  * { margin: 0; padding: 0; box-sizing: border-box; }
  html, body {
    width: 1200px; height: 1186px; overflow: hidden;
    background: var(--backdrop);
    font-family: "Open Sans", Arial, sans-serif;
  }
  .canvas { position: relative; width: 1200px; height: 1186px; }

  .card {
    position: absolute;
    width: 741px; height: 424px;
    border-radius: 42px;
    overflow: hidden;
  }
  .card-front { left: 122px; top: 156px; background: var(--paper); }
  .card-back  { left: 337px; top: 605px; background: var(--navy); }

  .side-tab {
    position: absolute; left: 0; top: 46px;
    width: 17px; height: 78px;
    background: var(--navy);
    border-radius: 0 6px 6px 0;
  }
  .holder-name {
    position: absolute; left: 49px; top: 58px;
    font-size: 25px; font-weight: 700; color: var(--navy);
  }
  .holder-title {
    position: absolute; left: 55px; top: 92px;
    font-size: 18px; color: var(--gold);
  }
  .address {
    position: absolute; left: 49px; top: 154px;
    font-size: 18px; line-height: 30px; color: var(--ink);
  }
  .contact-list {
    position: absolute; left: 49px; top: 256px;
    list-style: none;
    font-size: 18.5px; line-height: 28px; color: var(--ink);
  }
  .contact-list li { display: flex; align-items: center; gap: 12px; }
  .contact-list svg { width: 19px; height: 19px; fill: var(--gold); }

  .wordmark {
    position: absolute; left: 362px; top: 110px; width: 345px;
    text-align: center;
    font-size: 78px; font-weight: 600; letter-spacing: 2px;
    color: var(--navy); line-height: 1;
  }

  .footer-band { position: absolute; left: 0; top: 367px; width: 741px; height: 57px; }
  .footer-url {
    position: absolute; left: 49px; top: 374px;
    font-size: 16px; letter-spacing: 4px; color: #fbf3e0;
  }

  .back-wordmark {
    position: absolute; left: 0; width: 100%; top: 170px;
    text-align: center;
    font-size: 44px; font-weight: 600; letter-spacing: 1px;
    color: var(--gold); line-height: 1;
  }
  .back-url {
    position: absolute; left: 0; width: 100%; top: 242px;
    text-align: center;
    font-size: 23px; letter-spacing: 12px; color: #ffffff;
  }
</style>
</head>
<body>
<main class="canvas">
  <section class="card card-front">
    <div class="side-tab"></div>
    <h1 class="holder-name">Your Name</h1>
    <p class="holder-title">Title</p>
    <p class="address">Street Name, City Name,<br>Zip Code - 00000</p>
    <ul class="contact-list">
      <li>
        <svg viewBox="0 0 20 20" aria-hidden="true"><path d="M10 1a9 9 0 1 0 0 18 9 9 0 0 0 0-18zm0 1.6a7.4 7.4 0 1 1 0 14.8 7.4 7.4 0 0 1 0-14.8zM7.3 5.2c-.6.3-1.4 1.3-1.2 2.6.4 2.6 3.1 5.6 5.6 6.4 1.2.4 2.2-.3 2.6-.9l-1.7-1.6-1.1.7c-1-.4-2.3-1.9-2.6-3l.9-.9-1.2-2.1z"/></svg>
        <span>123-456-7890</span>
      </li>
      <li>
        <svg viewBox="0 0 20 20" aria-hidden="true"><path d="M6 1h8a1 1 0 0 1 1 1v16a1 1 0 0 1-1 1H6a1 1 0 0 1-1-1V2a1 1 0 0 1 1-1zm1 2v5h6V3H7zm0 7v2h2v-2H7zm3 0v2h2v-2h-2zm-3 3v2h2v-2H7zm3 0v2h2v-2h-2z"/></svg>
        <span>123-456-7890</span>
      </li>
      <li>
        <svg viewBox="0 0 20 20" aria-hidden="true"><path d="M2 8l8-5 8 5v9H2V8zm2 1.2v.3l6 4 6-4v-.3l-6-3.8-6 3.8z"/></svg>
        <span>info@halden.com</span>
      </li>
    </ul>
    <div class="wordmark">HALDEN</div>
    <svg class="footer-band" viewBox="0 0 741 57" aria-hidden="true">
      <rect x="0" y="0" width="741" height="57" fill="#14497c"/>
      <path d="M0 0 H497 C480 0 478 32 458 32 H0 Z" fill="#c0952f"/>
    </svg>
    <p class="footer-url">www.halden.com</p>
  </section>

  <section class="card card-back">
    <div class="back-wordmark">HALDEN</div>
    <p class="back-url">www.halden.com</p>
  </section>
</main>
</body>
</html>
```